Business Card Design for a Lending Business (Hard Money loans)

We need a business card for our Real Estate Lending business. We do hard Money loans for real estate investors. We have an existing logo we like, see attached. I'd like the business card to mostly include the logo colors, but a bright color pop of some sort would be nice to see also. Card should include Logo, Company Name, Company Address, Employee Name, Cell Phone, Main Phone, Email, Website

Industry/Entity Type

Finance / Lending

Contact Information for Business Card

Logo, Company Name, Company Address, Employee Name, Cell Phone, Main Phone, Email, Website

Requirements
Nice to have
• I'd like the business card to mostly include the logo colors, but a bright color pop of some sort would be nice to see also.

```html
<!DOCTYPE html>
<html lang="en">
<head>
<meta charset="utf-8">
<title>Harborline Lending – Business Card</title>
<link href="https://fonts.googleapis.com/css2?family=Montserrat:wght@400;500;700&display=swap" rel="stylesheet">
<style>
  :root {
    --bg: #1f2024;
    --cyan: #00aee0;
    --navy: #2b3786;
    --paper: #f4f5fa;
    --ink: #1c1c22;
    --white: #ffffff;
  }
  * { margin: 0; padding: 0; box-sizing: border-box; }
  html, body { width: 1200px; height: 900px; overflow: hidden; background: var(--bg); }
  body { font-family: "Montserrat", sans-serif; position: relative; }

  .card {
    position: absolute;
    left: 320px;
    width: 560px;
    height: 320px;
    overflow: hidden;
    box-shadow: 0 12px 30px rgba(0,0,0,0.45);
  }

  /* Front */
  .card-front { top: 90px; background: var(--cyan); display: flex; align-items: center; justify-content: center; }
  .brand { display: flex; align-items: center; gap: 16px; color: var(--white); }
  .brand-dot { width: 46px; height: 46px; border-radius: 50%; background: var(--white); }
  .brand-name { font-weight: 700; font-size: 30px; letter-spacing: 3px; line-height: 1.15; text-transform: uppercase; }

  /* Back */
  .card-back { top: 450px; background: var(--paper); }
  .card-back .shapes { position: absolute; inset: 0; }
  .badge {
    position: absolute; left: 410px; top: 18px;
    width: 116px; height: 116px; border-radius: 50%;
    background: var(--cyan);
    display: flex; align-items: center; justify-content: center; text-align: center;
    color: var(--white); font-weight: 700; font-size: 12px; letter-spacing: 1.5px; line-height: 1.3;
    text-transform: uppercase;
  }

  .contact { position: absolute; left: 44px; bottom: 22px; color: var(--ink); }
  .contact-name { color: var(--cyan); font-weight: 700; font-size: 22px; line-height: 1.2; }
  .contact-role { display: inline-block; font-size: 12px; font-weight: 500; margin: 2px 0 10px 4px; padding-bottom: 2px; border-bottom: 1.5px solid var(--navy); }
  .contact-list { list-style: none; font-size: 11.5px; line-height: 17px; }
  .contact-list li { display: flex; align-items: flex-start; gap: 10px; }
  .contact-list li.address { padding-left: 21px; }
  .contact-list svg { width: 11px; height: 11px; margin-top: 3px; flex: none; fill: var(--cyan); }
</style>
</head>
<body>

  <section class="card card-front">
    <div class="brand">
      <span class="brand-dot"></span>
      <span class="brand-name">Harborline<br>Lending</span>
    </div>
  </section>

  <section class="card card-back">
    <svg class="shapes" viewBox="0 0 560 320" width="560" height="320">
      <polygon points="300,0 560,0 560,170 480,140 395,230" fill="var(--navy)"/>
      <polygon points="300,0 420,40 395,230" fill="var(--cyan)"/>
      <polygon points="560,120 560,172 522,150" fill="var(--cyan)"/>
    </svg>
    <div class="badge">Harborline<br>Lending</div>

    <div class="contact">
      <h1 class="contact-name">Jonah Reyes</h1>
      <p class="contact-role">Owner</p>
      <ul class="contact-list">
        <li><svg viewBox="0 0 24 24"><path d="M6.6 10.8a15 15 0 0 0 6.6 6.6l2.2-2.2a1 1 0 0 1 1-.25 11.4 11.4 0 0 0 3.6.57 1 1 0 0 1 1 1V20a1 1 0 0 1-1 1A17 17 0 0 1 3 4a1 1 0 0 1 1-1h3.5a1 1 0 0 1 1 1c0 1.25.2 2.45.57 3.57a1 1 0 0 1-.25 1z"/></svg>877-555-0142</li>
        <li><svg viewBox="0 0 24 24"><path d="M7 1h10a2 2 0 0 1 2 2v18a2 2 0 0 1-2 2H7a2 2 0 0 1-2-2V3a2 2 0 0 1 2-2zm0 3v14h10V4z"/></svg>877-555-0143</li>
        <li><svg viewBox="0 0 24 24"><path d="M2 5h20v14H2zm2 2v.5l8 5 8-5V7z"/></svg>info@harborlinelending.com</li>
        <li><svg viewBox="0 0 24 24"><circle cx="12" cy="12" r="10"/></svg>www.harborlinelending.com</li>
        <li class="address">418 Maple Ridge Ave, #112<br>Oakdale, OH 43210</li>
      </ul>
    </div>
  </section>

</body>
</html>
```